Vornel Technologies business card design

We need a business card designed with our new logo. it would be great if the card could communicate it is a technology based company.

Target Market(s)

system integrators

Industry/Entity Type

technology, IOT

Contact Information for Business Card

Name, designation, Address, telephone number, email address

Requirements
Must have
• logo and company name
Nice to have
• something to do with technology

```html
<!DOCTYPE html>
<html lang="en">
<head>
<meta charset="utf-8">
<title>Vornel Technologies – Business Card</title>
<link href="https://fonts.googleapis.com/css2?family=Poppins:wght@400;600&display=swap" rel="stylesheet">
<style>
  :root {
    --page-bg: #1c1c1e;
    --card-bg: #3a3a3c;
    --card-edge: #f7931e;
    --accent: #f7931e;
    --text-light: #f2f2f2;
    --pattern-dark: #2e2e30;
    --pattern-light: #454548;
  }
  * { box-sizing: border-box; margin: 0; padding: 0; }
  html, body {
    width: 1200px; height: 900px; overflow: hidden;
    background: var(--page-bg);
    font-family: "Poppins", sans-serif;
  }
  .stage {
    width: 1200px; height: 900px;
    display: flex; flex-direction: column; align-items: center; justify-content: center;
    gap: 56px;
  }
  .card {
    position: relative;
    width: 540px; height: 308px;
    border-radius: 16px;
    background: var(--card-bg);
    border-bottom: 2px solid var(--card-edge);
    overflow: hidden;
  }

  /* Front */
  .card-front .accent-bar {
    position: absolute; left: 0; top: 48px;
    width: 7px; height: 40px; background: var(--accent);
  }
  .card-front .person { position: absolute; left: 30px; top: 44px; }
  .person-name {
    color: var(--accent); font-weight: 600; font-size: 25px;
    letter-spacing: 0.5px; text-transform: uppercase; line-height: 1.1;
  }
  .person-title {
    color: var(--text-light); font-size: 14px; letter-spacing: 1px;
    text-transform: uppercase; margin-top: 2px;
  }
  .divider {
    position: absolute; left: 30px; right: 30px; top: 124px;
    height: 1px; background: var(--accent);
  }
  .contact-list {
    position: absolute; left: 30px; top: 142px;
    list-style: none; color: var(--text-light); font-size: 14px; line-height: 1.65;
  }
  .contact-list li { display: flex; align-items: center; gap: 8px; }
  .contact-list svg { width: 12px; height: 12px; flex: none; }
  .brand {
    position: absolute; right: 30px; top: 64px;
    display: flex; align-items: center; gap: 10px;
  }
  .brand-mark { width: 16px; height: 16px; background: var(--accent); }
  .brand-name {
    color: var(--text-light); font-weight: 600; font-size: 19px;
    letter-spacing: 1px; text-transform: uppercase;
  }
  .address {
    position: absolute; right: 30px; bottom: 30px;
    text-align: right; color: var(--text-light); font-size: 14px; line-height: 1.5;
  }

  /* Back */
  .card-back .pattern {
    position: absolute; inset: 0;
    background: linear-gradient(135deg, var(--pattern-light) 0%, var(--pattern-dark) 55%, var(--pattern-light) 100%);
  }
  .card-back .brand { top: auto; bottom: 28px; }
  .card-back .brand-name { font-size: 15px; }
  .card-back .brand-mark { width: 13px; height: 13px; }
</style>
</head>
<body>
<main class="stage">
  <section class="card card-front" aria-label="Business card front">
    <span class="accent-bar"></span>
    <div class="person">
      <p class="person-name">Daniel Hartwig</p>
      <p class="person-title">Director</p>
    </div>
    <div class="brand">
      <span class="brand-mark"></span>
      <span class="brand-name">Vornel Technologies</span>
    </div>
    <div class="divider"></div>
    <ul class="contact-list">
      <li>
        <svg viewBox="0 0 12 12"><path d="M2.5 1h2l1 2.5-1.3 1a6 6 0 0 0 3.3 3.3l1-1.3L11 7.5v2a1 1 0 0 1-1 1A9 9 0 0 1 1.5 2a1 1 0 0 1 1-1z" fill="var(--accent)"/></svg>
        (555) 014-7732
      </li>
      <li>
        <svg viewBox="0 0 12 12"><rect x="1" y="2.5" width="10" height="7" fill="none" stroke="var(--accent)"/><path d="M1 2.5l5 4 5-4" fill="none" stroke="var(--accent)"/></svg>
        info@vorneltech.com
      </li>
      <li>
        <svg viewBox="0 0 12 12"><circle cx="6" cy="6" r="5" fill="none" stroke="var(--accent)"/><ellipse cx="6" cy="6" rx="2.2" ry="5" fill="none" stroke="var(--accent)"/><path d="M1 6h10" stroke="var(--accent)"/></svg>
        vorneltechnologies.com
      </li>
    </ul>
    <p class="address">417 Alder Lane<br>Fairbrook, MI 49021</p>
  </section>

  <section class="card card-back" aria-label="Business card back">
    <div class="pattern" role="img" aria-label="Repeating embossed brand-mark pattern in dark greys"></div>
    <div class="brand">
      <span class="brand-mark"></span>
      <span class="brand-name">Vornel Technologies</span>
    </div>
  </section>
</main>
</body>
</html>
```